QXT website video quote promotion tiles

We are promoting vehicle leasing by video, which contains several quotation examples imported from the video. We must re-vamp the quotation tiles, contact boxes, and contact form. The first tile is generated from the video, so this must be a separate project. We are looking for a welcoming, professional flow and leave color choices to design with an emphasis on communication prompts, and additional prompts in the design would be welcome.

Target Market(s)

Any Customer interaction from the tile quotes, contact, call, message,

Industry/Entity Type

vehicle leasing

Coding

Coded - Design and coding required

Number of Pages Required

1 page

Colors

Designer to choose colors to be used in the design.

Requirements
Must have
• emphasis on point of contact and visual impact on quote tile excluding main one
Should not have
• changes to the quote structure as these imported from video pricing no changes to main image as this template which can addressed as separate project

```html
<!DOCTYPE html>
<html lang="en">
<head>
<meta charset="UTF-8">
<title>QXT Contract Hire Quote Tiles</title>
<link href="https://fonts.googleapis.com/css2?family=Poppins:wght@400;500;600;700&display=swap" rel="stylesheet">
<style>
:root{
  --page:#f0f0f0;
  --white:#ffffff;
  --ink:#111111;
  --muted:#555555;
  --alert:#d0021b;
  --blue-dark:#3d74bb;
  --blue-light:#56c2ef;
  --gold-top:#f4c655;
  --gold-bottom:#eea64a;
  --green:#1fa51f;
  --field:#f8f8f8;
  --field-line:#e2e2e2;
  --frame-grey:#c4c4c8;
}
*{box-sizing:border-box;margin:0;padding:0}
html,body{width:1061px;height:1200px;overflow:hidden}
body{background:var(--page);font-family:'Poppins',sans-serif;position:relative;color:var(--ink)}
.abs{position:absolute}
.tile{position:absolute;background:var(--white);border-radius:16px;box-shadow:0 6px 20px rgba(0,0,0,.05)}
.tile-title{font-weight:700;font-size:17px;letter-spacing:-.2px}
.tile-terms{font-size:13px;color:var(--muted)}
.tile-status{font-size:11px;color:var(--alert)}
.btn-contact{position:absolute;width:172px;height:39px;border-radius:20px;border:0;
  background:linear-gradient(var(--gold-top),var(--gold-bottom));color:var(--white);
  font:700 13.5px 'Poppins',sans-serif;display:flex;align-items:center;justify-content:center}
.btn-call{position:absolute;width:40px;height:40px;border-radius:50%;background:var(--green);
  display:flex;align-items:center;justify-content:center}
.price{font-weight:700;color:var(--white);line-height:1}
.vat{font-size:7.5px;color:var(--white);font-weight:600;letter-spacing:.3px}

/* ribbon tile */
.ribbon{left:240px;top:115px;width:67px;height:87px;background:linear-gradient(var(--blue-light),var(--blue-dark));
  clip-path:polygon(0 0,100% 0,100% 100%,50% 84%,0 100%);text-align:center;padding-top:27px}
.ribbon-fold{left:227px;top:115px;width:0;height:0;border-left:13px solid transparent;border-bottom:15px solid var(--blue-dark)}
.service-icon{left:82px;top:144px;width:36px;height:36px;border-radius:50%;background:#e9ecef}

/* header tile */
.framed{position:absolute;left:383px;top:123px;width:271px;height:222px;background:var(--white);
  border-left:5px solid var(--frame-grey);border-bottom:5px solid var(--frame-grey);border-bottom-right-radius:28px;
  box-shadow:3px 0 0 var(--frame-grey)}
.header-pill{left:380px;top:123px;width:215px;height:51px;border-radius:26px 0 0 26px;
  background:linear-gradient(90deg,var(--blue-light),var(--blue-dark));color:var(--white);
  font-weight:700;font-size:16.5px;display:flex;align-items:center;padding-left:28px}
.price-disc{left:569px;top:89px;width:122px;height:122px;border-radius:50%;
  background:linear-gradient(160deg,var(--blue-light),var(--blue-dark));display:flex;align-items:center;justify-content:center}
.price-disc-inner{width:104px;height:104px;border-radius:50%;background:var(--white);text-align:center;padding-top:32px}

/* centred tile */
.badge{left:816px;top:187px;width:90px;height:90px;border-radius:50%;
  background:linear-gradient(var(--blue-light),var(--blue-dark));display:flex;align-items:center;justify-content:center}
.badge-ring{width:82px;height:82px;border-radius:50%;border:1.5px solid var(--white);text-align:center;padding-top:23px}

/* form */
.contact-form{left:268px;top:499px;width:525px;height:543px;background:var(--white);border-radius:35px;overflow:hidden}
.form-head{height:71px;background:linear-gradient(90deg,var(--blue-dark),var(--blue-light));display:flex;align-items:center;justify-content:center;position:relative}
.form-head h1{font-size:21px;font-weight:700;color:var(--white);letter-spacing:-.2px}
.form-close{position:absolute;right:23px;top:25px}
.field{position:absolute;left:28px;width:468px;height:43px;border-radius:22px;background:var(--field);border:1px solid var(--field-line);
  font-size:11px;color:#222;padding:0 18px;display:flex;align-items:center}
.field.msg{height:135px;border-radius:30px;align-items:flex-start;padding-top:14px}
.btn-submit{position:absolute;left:29px;top:457px;width:467px;height:39px;border-radius:20px;
  background:linear-gradient(var(--gold-top),var(--gold-bottom));color:var(--white);font-weight:700;font-size:13.5px;
  display:flex;align-items:center;justify-content:center}
</style>
</head>
<body>
<svg width="0" height="0" style="position:absolute">
  <symbol id="phone" viewBox="0 0 24 24"><path fill="#fff" d="M6.6 10.8a15.1 15.1 0 0 0 6.6 6.6l2.2-2.2a1 1 0 0 1 1-.25 11.4 11.4 0 0 0 3.6.57 1 1 0 0 1 1 1V20a1 1 0 0 1-1 1A17 17 0 0 1 3 4a1 1 0 0 1 1-1h3.5a1 1 0 0 1 1 1c0 1.25.2 2.45.57 3.57a1 1 0 0 1-.25 1z"/></symbol>
</svg>

<!-- Tile 1: ribbon -->
<div class="tile" style="left:57px;top:130px;width:273px;height:215px"></div>
<div class="abs ribbon-fold"></div>
<div class="abs ribbon"><div class="price" style="font-size:14px">£249.27</div><div class="vat">PLUS VAT</div></div>
<div class="abs service-icon" role="img" aria-label="Service icon"></div>
<div class="abs tile-title" style="left:82px;top:184px">CONTRACT HIRE</div>
<div class="abs tile-terms" style="left:82px;top:221px">3 years, 9+35, 10K miles annually</div>
<div class="abs tile-status" style="left:82px;top:245px">Not Maintained</div>
<div class="btn-contact" style="left:82px;top:282px">Contact Us</div>
<div class="btn-call" style="left:267px;top:282px"><svg width="18" height="18"><use href="#phone"/></svg></div>

<!-- Tile 2: header pill -->
<div class="framed"></div>
<div class="abs header-pill">CONTRACT HIRE</div>
<div class="abs price-disc"><div class="price-disc-inner"><div style="font-weight:700;font-size:20px;line-height:1">£249.27</div><div style="font-size:8.5px;color:var(--muted);margin-top:5px">PLUS VAT</div></div></div>
<div class="abs tile-terms" style="left:401px;top:213px">3 years, 9+35, 10K miles annually</div>
<div class="abs tile-status" style="left:401px;top:238px">Not Maintained</div>
<div class="btn-contact" style="left:401px;top:274px">Contact Us</div>
<div class="btn-call" style="left:586px;top:274px"><svg width="18" height="18"><use href="#phone"/></svg></div>

<!-- Tile 3: centred badge -->
<div class="tile" style="left:724px;top:130px;width:273px;height:281px"></div>
<div class="abs tile-title" style="left:724px;width:273px;text-align:center;top:150px">CONTRACT HIRE</div>
<div class="abs badge"><div class="badge-ring"><div class="price" style="font-size:16px">£249.27</div><div class="vat" style="font-size:8px;font-weight:500;margin-top:4px">PLUS VAT</div></div></div>
<div class="abs tile-terms" style="left:724px;width:273px;text-align:center;top:292px">3 years, 9+35, 10K miles annually</div>
<div class="abs tile-status" style="left:724px;width:273px;text-align:center;top:315px">Not Maintained</div>
<div class="btn-contact" style="left:749px;top:346px">Contact Us</div>
<div class="btn-call" style="left:933px;top:346px"><svg width="18" height="18"><use href="#phone"/></svg></div>

<!-- Contact form -->
<div class="abs contact-form">
  <div class="form-head">
    <h1>Please submit your contact details</h1>
    <svg class="form-close" width="22" height="22" viewBox="0 0 22 22"><circle cx="11" cy="11" r="10" fill="none" stroke="#fff" stroke-width="1.6"/><path d="M7 7l8 8M15 7l-8 8" stroke="#fff" stroke-width="1.6"/></svg>
  </div>
  <div class="field" style="top:107px">Your Name</div>
  <div class="field" style="top:169px">Email</div>
  <div class="field" style="top:230px">Contact Number</div>
  <div class="field msg" style="top:292px">Message</div>
  <div class="btn-submit">Submit Now</div>
</div>
</body>
</html>
```